KalVesta Website- Joomla Template

A website for a Plumber company. A one page design ( this is what i mean http://pallowdesign.example/en/#graph)
The website should be a template for Joomla, i will do the website in 3 languages
I want it to be elegant but not so that it looks like a consulting company.
My customers are private customers, my products are :
Main focus is on Fixing 24/7
then renovate bathrooms
replace heating systems
and Maintenance
I need 12 slides:
Who we are
News
Service
Maintenance
Renewable Energy
Sanitary
Heating
Ventilation
Partners
Useful Links
Contact us
of course a Facebook, twitter and G+ icon
try to make an innovative nice menu

```html
<!DOCTYPE html>
<html lang="en">
<head>
<meta charset="utf-8">
<title>KalVesta — Plumbing, Heating &amp; Sanitary</title>
<link href="https://fonts.googleapis.com/css2?family=Open+Sans:wght@400;600;700&family=PT+Serif:wght@400;700&display=swap" rel="stylesheet">
<style>
:root{
  --blue:#2b6aa6;
  --blue-dark:#1f4f7d;
  --green:#6cbf4a;
  --ink:#333a40;
  --text:#6b7177;
  --muted:#9aa0a6;
  --line:#e2e5e8;
  --panel:#f3f4f5;
  --white:#ffffff;
  --dark-strip:rgba(40,44,48,.82);
  --sans:"Open Sans", Arial, sans-serif;
  --serif:"PT Serif", Georgia, serif;
}
*{box-sizing:border-box;margin:0;padding:0}
html,body{width:1200px;height:3552px;overflow:hidden;background:var(--white)}
body{position:relative;font-family:var(--sans);color:var(--text)}
section,header,nav,footer{position:absolute;left:0;width:1200px}

/* HERO */
.hero{top:0;height:600px}
.hero-photo{position:absolute;inset:0;background:linear-gradient(180deg,#e9eaeb 0%,#d6d8da 45%,#b9bcbf 70%,#a6a9ac 100%)}
.hero-brand{position:absolute;top:40px;left:0;width:1200px;height:360px;background:rgba(255,255,255,.55);display:flex;flex-direction:column;align-items:center;justify-content:center}
.brand-lockup{display:flex;align-items:center;gap:18px}
.brand-dot{width:22px;height:22px;border-radius:50%;background:var(--blue-dark)}
.brand-name{font-family:var(--serif);font-size:58px;letter-spacing:6px;color:var(--blue-dark);font-weight:400;line-height:1}
.brand-tagline{font-family:var(--sans);font-size:15px;letter-spacing:4px;color:var(--ink);margin-top:18px}
.hero-strip{position:absolute;top:420px;left:0;width:1200px;height:56px;background:var(--dark-strip)}
.slider-dots{position:absolute;top:24px;left:570px;display:flex;gap:10px}
.slider-dots span{width:9px;height:9px;border-radius:50%;background:#888}
.slider-dots span.active{background:var(--white)}
.badge-247{position:absolute;top:400px;left:925px;width:96px;height:96px;border-radius:50%;border:2px solid var(--white);color:var(--white);font-family:var(--serif);font-size:17px;text-align:center;line-height:20px;padding-top:26px}
.scroll-hint{position:absolute;top:400px;left:1110px}

/* NAV */
.main-nav{top:600px;height:64px;background:var(--panel);border-bottom:1px solid var(--line)}
.main-nav ul{list-style:none;display:flex;align-items:center;justify-content:center;height:64px;gap:46px}
.main-nav a{font-size:12px;font-weight:600;color:var(--ink);text-decoration:none;letter-spacing:.5px}
.nav-brand{font-family:var(--serif);font-size:18px;letter-spacing:2px;color:var(--blue-dark)}

/* Shared headings */
.section-title{font-family:var(--sans);font-size:40px;font-weight:400;color:var(--blue);text-align:center;letter-spacing:1px}
.section-title::after{content:"";display:block;width:90px;height:3px;background:var(--green);margin:8px auto 0}
.section-title.on-photo{color:var(--ink)}

/* WHO WE ARE */
.about{top:700px;height:240px;text-align:center}
.about p{width:860px;margin:14px auto 0;font-size:12px;line-height:18px;font-family:var(--serif)}

/* NEWS */
.news{top:948px;height:372px}
.news-photo{position:absolute;inset:0;background:linear-gradient(90deg,#cfc9c2 0%,#e6e4e1 40%,#d4d6d8 100%)}
.news .section-title{position:relative;padding-top:34px}
.news-cards{position:absolute;top:130px;left:165px;display:flex;gap:22px}
.news-card{width:152px;height:200px;background:var(--white);border-top:4px solid var(--green);text-align:center;padding:18px 12px}
.news-card h3{font-family:var(--serif);font-size:14px;color:var(--ink);font-weight:700}
.news-card p{font-size:10px;line-height:14px;margin-top:8px;font-family:var(--serif)}
.btn-small{display:inline-block;margin-top:18px;background:var(--green);color:var(--white);font-size:9px;font-weight:700;padding:5px 12px;border-radius:2px}

/* SERVICES */
.services{top:1360px;height:640px}
.services .intro{width:760px;margin:14px auto 0;text-align:center;font-size:12px;line-height:18px;font-family:var(--serif)}
.service-grid{position:absolute;top:120px;left:140px;display:grid;grid-template-columns:repeat(3,280px);gap:40px 20px}
.service{height:240px;background:var(--panel);text-align:center;padding:24px 22px}
.service svg{display:block;margin:0 auto}
.service h3{font-family:var(--serif);font-weight:400;font-size:22px;color:var(--ink);margin-top:12px}
.service p{font-size:11px;line-height:16px;margin-top:10px;font-family:var(--serif)}

/* PARTNERS */
.partners{top:2020px;height:360px}
.partners-photo{position:absolute;inset:0;background:linear-gradient(90deg,#d9d4cc 0%,#ecebe8 50%,#d2d4d6 100%)}
.partners .section-title{position:relative;padding-top:20px}
.partner-cards{position:absolute;top:110px;left:150px;display:flex;gap:12px}
.partner{width:216px;background:var(--white)}
.partner-photo{height:150px;background:linear-gradient(180deg,#9fb3c6,#6e7f8f)}
.partner-info{text-align:center;padding:16px 0 20px}
.partner-name{font-family:var(--serif);font-size:20px;color:var(--ink)}
.partner-role{font-size:9px;color:var(--muted);letter-spacing:1px;margin-top:4px}

/* LINKS */
.links{top:2400px;height:250px;text-align:center}
.links ul{list-style:none;margin-top:26px}
.links li{font-family:var(--serif);font-size:12px;line-height:26px;color:var(--ink)}
.links li.highlight{color:var(--blue);text-decoration:underline}

/* CONTACT */
.contact{top:2660px;height:830px}
.contact-map{position:absolute;top:66px;left:0;width:1200px;height:440px;background:linear-gradient(180deg,#d7d9db,#c4c7ca)}
.contact-row{position:absolute;top:520px;left:0;width:1200px;display:flex;justify-content:space-around;padding:0 120px;font-family:var(--serif);font-size:20px;color:var(--ink);border-bottom:1px solid var(--line);height:50px}
.contact-row span{display:flex;align-items:center;gap:10px;height:36px}
.contact-form{position:absolute;top:600px;left:280px;width:640px;display:grid;grid-template-columns:260px 320px;gap:0 40px}
.field{height:36px;border:1px solid var(--line);margin-bottom:12px;font-size:12px;color:var(--muted);padding:10px}
.field.message{height:132px}
.captcha{display:flex;gap:10px;align-items:center;font-size:12px}
.captcha b{font-family:var(--serif);color:#c4443a;font-style:italic;font-weight:400}
.btn-send{background:var(--green);color:var(--white);font-size:10px;font-weight:700;padding:8px 16px;border-radius:2px}

/* FOOTER */
.site-footer{top:3496px;height:56px;text-align:center}
.social{display:flex;justify-content:center;gap:12px}
.social span{width:22px;height:22px;border-radius:50%;background:#c9ccd0}
.social span.mid{background:var(--blue)}
.copyright{font-size:8px;color:var(--muted);margin-top:6px;letter-spacing:1px}
</style>
</head>
<body>

<header class="hero">
  <div class="hero-photo" role="img" aria-label="Greyscale photo of a plumber fitting pipes"></div>
  <div class="hero-brand">
    <div class="brand-lockup">
      <span class="brand-dot"></span>
      <span class="brand-name">KalVesta</span>
    </div>
    <div class="brand-tagline">CRAFT YOU CAN COUNT ON</div>
  </div>
  <div class="hero-strip">
    <div class="slider-dots"><span class="active"></span><span></span><span></span><span></span></div>
  </div>
  <div class="badge-247">FIXING<br>24/7</div>
  <svg class="scroll-hint" width="30" height="110" viewBox="0 0 30 110"><line x1="15" y1="10" x2="15" y2="100" stroke="#fff" stroke-width="2"/><polyline points="8,18 15,8 22,18" fill="none" stroke="#fff" stroke-width="2"/><polyline points="8,92 15,102 22,92" fill="none" stroke="#fff" stroke-width="2"/></svg>
</header>

<nav class="main-nav">
  <ul>
    <li><a href="#about">WHO WE ARE</a></li>
    <li><a href="#news">NEWS</a></li>
    <li><a href="#services">OUR SERVICES ▾</a></li>
    <li><span class="nav-brand">KalVesta</span></li>
    <li><a href="#partners">PARTNERS</a></li>
    <li><a href="#links">USEFUL LINKS</a></li>
    <li><a href="#contact">CONTACT US</a></li>
  </ul>
</nav>

<section class="about" id="about">
  <h2 class="section-title">WHO WE ARE</h2>
  <p>Lorem ipsum dolor sit amet, consectetuer adipiscing elit, sed diam nonummy nibh euismod tincidunt ut laoreet dolore magna aliquam erat volutpat. Ut wisi enim ad minim veniam, quis nostrud exerci tation ullamcorper suscipit lobortis nisl ut aliquip ex ea commodo consequat. Duis autem vel eum iriure dolor in hendrerit in vulputate velit esse molestie consequat, vel illum dolore eu feugiat nulla facilisis at vero eros et accumsan.</p>
  <p>Etiam dolore eu feugiat nulla facilisis at vero eros et accumsan et iusto odio dignissim qui blandit praesent luptatum zzril delenit augue duis.</p>
</section>

<section class="news" id="news">
  <div class="news-photo" role="img" aria-label="Photo of hands working on a pipe fitting"></div>
  <h2 class="section-title on-photo">NEWS</h2>
  <div class="news-cards">
    <article class="news-card"><h3>Latest News</h3><p>Dignissim qui blandit praesent luptatum zzril delenit augue duis dolore te feugait.</p><span class="btn-small">READ MORE</span></article>
    <article class="news-card"><h3>Latest News</h3><p>Dignissim qui blandit praesent luptatum zzril delenit augue duis dolore te feugait.</p><span class="btn-small">READ MORE</span></article>
    <article class="news-card"><h3>Latest News</h3><p>Dignissim qui blandit praesent luptatum zzril delenit augue duis dolore te feugait.</p><span class="btn-small">READ MORE</span></article>
    <article class="news-card"><h3>Latest News</h3><p>Dignissim qui blandit praesent luptatum zzril delenit augue duis dolore te feugait.</p><span class="btn-small">READ MORE</span></article>
    <article class="news-card"><h3>Latest News</h3><p>Dignissim qui blandit praesent luptatum zzril delenit augue duis dolore te feugait.</p><span class="btn-small">READ MORE</span></article>
  </div>
</section>

<section class="services" id="services">
  <h2 class="section-title">OUR SERVICES</h2>
  <p class="intro">Etiam dolore eu feugiat nulla facilisis at vero eros et accumsan et iusto odio dignissim qui blandit praesent luptatum zzril delenit augue duis dolore.</p>
  <div class="service-grid">
    <div class="service">
      <svg width="64" height="64" viewBox="0 0 64 64"><circle cx="32" cy="32" r="30" fill="none" stroke="#333a40" stroke-width="3"/><line x1="20" y1="44" x2="42" y2="22" stroke="#333a40" stroke-width="6" stroke-linecap="round"/><circle cx="44" cy="20" r="7" fill="none" stroke="#333a40" stroke-width="4"/></svg>
      <h3>Service Maintenance</h3>
      <p>Lorem ipsum dolor sit amet, consectetuer adipiscing elit. Nam vel turpis. Duis at turpis ut lorem viverra sagittis.</p>
    </div>
    <div class="service">
      <svg width="64" height="64" viewBox="0 0 64 64"><path d="M14 22h26v8H22v20h-8z" fill="#333a40"/><rect x="24" y="12" width="16" height="5" fill="#333a40"/><rect x="30" y="16" width="4" height="7" fill="#333a40"/></svg>
      <h3>Sanitary</h3>
      <p>Lorem ipsum dolor sit amet, consectetuer adipiscing elit. Nam vel turpis. Duis at turpis ut lorem viverra sagittis.</p>
    </div>
    <div class="service">
      <svg width="64" height="64" viewBox="0 0 64 64"><circle cx="32" cy="32" r="30" fill="#333a40"/><circle cx="32" cy="32" r="10" fill="#fff"/><g stroke="#fff" stroke-width="3"><line x1="32" y1="10" x2="32" y2="18"/><line x1="32" y1="46" x2="32" y2="54"/><line x1="10" y1="32" x2="18" y2="32"/><line x1="46" y1="32" x2="54" y2="32"/></g></svg>
      <h3>Renewable Energy</h3>
      <p>Lorem ipsum dolor sit amet, consectetuer adipiscing elit. Nam vel turpis. Duis at turpis ut lorem viverra sagittis.</p>
    </div>
    <div class="service">
      <svg width="64" height="64" viewBox="0 0 64 64"><circle cx="32" cy="32" r="30" fill="none" stroke="#333a40" stroke-width="3"/><path d="M32 14c8 10 12 16 12 24a12 12 0 0 1-24 0c0-6 4-10 6-14 2 4 4 6 6 6 0-6-2-10 0-16z" fill="#333a40"/></svg>
      <h3>Heating</h3>
      <p>Lorem ipsum dolor sit amet, consectetuer adipiscing elit. Nam vel turpis. Duis at turpis ut lorem viverra sagittis.</p>
    </div>
    <div class="service">
      <svg width="64" height="64" viewBox="0 0 64 64"><circle cx="32" cy="32" r="30" fill="none" stroke="#333a40" stroke-width="3"/><g fill="#333a40"><ellipse cx="32" cy="20" rx="6" ry="11"/><ellipse cx="32" cy="44" rx="6" ry="11"/><ellipse cx="20" cy="32" rx="11" ry="6"/><ellipse cx="44" cy="32" rx="11" ry="6"/></g><circle cx="32" cy="32" r="4" fill="#fff"/></svg>
      <h3>Ventilation</h3>
      <p>Lorem ipsum dolor sit amet, consectetuer adipiscing elit. Nam vel turpis. Duis at turpis ut lorem viverra sagittis.</p>
    </div>
    <div class="service">
      <svg width="64" height="64" viewBox="0 0 64 64"><circle cx="32" cy="32" r="30" fill="#333a40"/><g stroke="#fff" stroke-width="3" stroke-linecap="round"><line x1="32" y1="12" x2="32" y2="52"/><line x1="15" y1="22" x2="49" y2="42"/><line x1="15" y1="42" x2="49" y2="22"/></g></svg>
      <h3>Air Conditioning</h3>
      <p>Lorem ipsum dolor sit amet, consectetuer adipiscing elit. Nam vel turpis. Duis at turpis ut lorem viverra sagittis.</p>
    </div>
  </div>
</section>

<section class="partners" id="partners">
  <div class="partners-photo" role="img" aria-label="Photo of a bright workshop interior"></div>
  <h2 class="section-title on-photo">PARTNERS</h2>
  <div class="partner-cards">
    <div class="partner"><div class="partner-photo" role="img" aria-label="Portrait of a partner in a hard hat"></div><div class="partner-info"><div class="partner-name">JOHN DOE</div><div class="partner-role">PARTNER</div></div></div>
    <div class="partner"><div class="partner-photo" role="img" aria-label="Portrait of a partner in work clothes"></div><div class="partner-info"><div class="partner-name">JOHN DOE</div><div class="partner-role">PARTNER</div></div></div>
    <div class="partner"><div class="partner-photo" role="img" aria-label="Portrait of a partner in a hard hat"></div><div class="partner-info"><div class="partner-name">JOHN DOE</div><div class="partner-role">PARTNER</div></div></div>
    <div class="partner"><div class="partner-photo" role="img" aria-label="Portrait of a partner in work clothes"></div><div class="partner-info"><div class="partner-name">JOHN DOE</div><div class="partner-role">PARTNER</div></div></div>
  </div>
</section>

<section class="links" id="links">
  <h2 class="section-title">LINKS</h2>
  <ul>
    <li>Lorem Ipsum</li>
    <li>Dolor Sit Amet</li>
    <li>Santa in Mantle Porta Viverra</li>
    <li class="highlight">Santa in Mantle Porta Viverra</li>
    <li>Consectetuer Elit</li>
  </ul>
</section>

<section class="contact" id="contact">
  <h2 class="section-title">CONTACT US</h2>
  <div class="contact-map" role="img" aria-label="Greyscale world map showing the office location"></div>
  <div class="contact-row">
    <span><svg width="16" height="22" viewBox="0 0 16 22"><path d="M8 0a8 8 0 0 1 8 8c0 6-8 14-8 14S0 14 0 8a8 8 0 0 1 8-8z" fill="#333a40"/><circle cx="8" cy="8" r="3" fill="#fff"/></svg>CITY, XYZ</span>
    <span><svg width="20" height="20" viewBox="0 0 20 20"><path d="M4 1l4 4-2 3q2 4 6 6l3-2 4 4-3 3Q8 19 1 4z" fill="#333a40"/></svg>32 41 55 210</span>
    <span><svg width="22" height="16" viewBox="0 0 22 16"><rect width="22" height="16" fill="#333a40"/><polyline points="1,1 11,9 21,1" fill="none" stroke="#fff" stroke-width="1.5"/></svg>info@kalvesta.example</span>
  </div>
  <form class="contact-form">
    <div>
      <div class="field">Name</div>
      <div class="field">Email</div>
      <div class="field">Phone</div>
      <div class="captcha"><b>Wacfe</b><div class="field" style="margin:0;flex:1">Insert Captcha</div></div>
    </div>
    <div>
      <div class="field message">Message</div>
      <div style="display:flex;justify-content:flex-end;margin-top:40px"><span class="btn-send">SEND MESSAGE</span></div>
    </div>
  </form>
</section>

<footer class="site-footer">
  <div class="social"><span></span><span class="mid"></span><span></span></div>
  <div class="copyright">COPYRIGHT © 2024 KALVESTA. ALL RIGHTS RESERVED.</div>
</footer>

</body>
</html>
```